Morvane Estates Business Card and Email Signature Design

I am a Brokiva and need a business card design with my head shot picture and logo and contact information that can be prepared to be used on my email signature as well. I would like my head shot image background to match the background of the business card. So in other words the background of my head shot should be transparent. I would like the Brokiva Logo on there and also ListNest and Civic Nestmark Logo. My email address is: lina@morvaneestates.example, Phone Number is: 555-614-7290, website: www.morvaneestates.example Address: 20874 Quillfeather Court Harrowgate, KS 47518
I also need just the head shot photo with white background in a JPEG file as well so I can upload that picture to my ProfLoop and Hausora profiles.

```html
<!DOCTYPE html>
<html lang="en">
<head>
<meta charset="utf-8">
<title>Morvane Estates Business Card</title>
<link rel="stylesheet" href="https://fonts.googleapis.com/css2?family=Roboto:wght@400;500&family=Roboto+Condensed:wght@500;700&display=swap">
<style>
  :root {
    --stage: #2a2a2a;
    --brand-blue: #06527a;
    --brand-grey: #4a4a4a;
    --disc: #eeeeee;
    --card-white: #f1f1f1;
    --ink-light: #ffffff;
    --ink-muted: #5a5a5a;
    --photo-top: #7d8a96;
    --photo-bottom: #1f2a3a;
  }
  * { margin: 0; padding: 0; box-sizing: border-box; }
  html, body { width: 1200px; height: 960px; overflow: hidden; background: var(--stage); }
  .stage { position: relative; width: 1200px; height: 960px; }

  .card {
    position: absolute; width: 600px; height: 342px;
    border-radius: 18px; overflow: hidden;
  }
  .card--front { left: 314px; top: 113px; background: var(--brand-blue); }
  .card--back { left: 311px; top: 472px; background: var(--card-white); }

  .front-backdrop { position: absolute; inset: 0; }

  .headshot {
    position: absolute; left: 41px; top: 39px; width: 70px; height: 90px;
    border: 1.5px solid #c9d3dc; border-radius: 3px;
    background: linear-gradient(180deg, var(--photo-top), var(--photo-bottom));
  }
  .identity { position: absolute; left: 129px; top: 60px; color: var(--ink-light);
    font-family: "Roboto Condensed", sans-serif; font-weight: 500; }
  .identity__name { font-size: 21px; letter-spacing: 0.2px; line-height: 1.1; }
  .identity__title { font-size: 15px; line-height: 1.3; }

  .badges { position: absolute; left: 40px; top: 150px; display: flex; align-items: flex-end; gap: 5px; }
  .badge { background: var(--ink-light); }
  .badge--housing { width: 39px; height: 37px; border-radius: 2px; }
  .badge--listing { width: 54px; height: 27px; border-radius: 2px; }

  .address, .contact { position: absolute; left: 39px; color: var(--ink-light);
    font-family: "Roboto", sans-serif; font-size: 14px; }
  .address { top: 200px; line-height: 18.5px; }
  .contact { top: 244px; list-style: none; line-height: 19px; }
  .contact li { display: flex; align-items: center; gap: 6px; }
  .contact svg { width: 14px; height: 14px; flex: none; fill: var(--ink-light); }

  .brand-front { position: absolute; left: 315px; top: 92px; width: 230px; text-align: center; }
  .brand-mark { display: block; margin: 0 auto 6px; border-radius: 50%; background: var(--brand-blue); }
  .brand-front .brand-mark { width: 78px; height: 78px; }
  .brand-name { font-family: "Roboto Condensed", sans-serif; font-weight: 700; color: var(--brand-blue);
    letter-spacing: 0.5px; white-space: nowrap; }
  .brand-front .brand-name { font-size: 24px; }

  .brand-back { position: absolute; left: 0; right: 0; top: 84px; text-align: center; }
  .brand-back .brand-mark { width: 100px; height: 100px; margin-bottom: 10px; }
  .brand-back .brand-name { font-size: 30px; }
  .website-back { position: absolute; left: 0; right: 0; top: 287px; text-align: center;
    font-family: "Roboto", sans-serif; font-size: 14px; letter-spacing: 3.6px; color: var(--ink-muted); }
</style>
</head>
<body>
<main class="stage">
  <section class="card card--front" aria-label="Business card front">
    <svg class="front-backdrop" viewBox="0 0 600 342" width="600" height="342" aria-hidden="true">
      <rect x="430" y="0" width="170" height="342" fill="var(--brand-grey)"/>
      <circle cx="427" cy="171" r="172" fill="var(--disc)"/>
    </svg>

    <div class="headshot" role="img" aria-label="Head shot of Lina Varrow"></div>
    <div class="identity">
      <p class="identity__name">LINA VARROW</p>
      <p class="identity__title">CEO/FOUNDER</p>
    </div>

    <div class="badges">
      <span class="badge badge--housing" role="img" aria-label="Civic Nestmark badge"></span>
      <span class="badge badge--listing" role="img" aria-label="Brokiva and ListNest badge"></span>
    </div>

    <p class="address">20874 Quillfeather<br>Court Harrowgate, KS 47518</p>

    <ul class="contact">
      <li><svg viewBox="0 0 24 24" aria-hidden="true"><path d="M6.6 10.8a15.1 15.1 0 0 0 6.6 6.6l2.2-2.2a1 1 0 0 1 1-.25 11.4 11.4 0 0 0 3.6.57 1 1 0 0 1 1 1V20a1 1 0 0 1-1 1A17 17 0 0 1 3 4a1 1 0 0 1 1-1h3.5a1 1 0 0 1 1 1c0 1.25.2 2.45.57 3.57a1 1 0 0 1-.25 1z"/></svg>555-614-7290</li>
      <li><svg viewBox="0 0 24 24" aria-hidden="true"><path d="M2 6.5 12 13l10-6.5V19H2z"/><path d="M2 5h20l-10 6.5z"/></svg>lina@morvaneestates.example</li>
      <li><svg viewBox="0 0 24 24" aria-hidden="true"><circle cx="12" cy="12" r="10"/><path d="M7 7c2 1 2 3 4 3s1 3 3 3-1 4-2 5M15 4c-1 2 1 3 3 3" fill="none" stroke="#06527a" stroke-width="1.6"/></svg>www.morvaneestates.example</li>
    </ul>

    <div class="brand-front">
      <span class="brand-mark"></span>
      <p class="brand-name">MORVANE ESTATES</p>
    </div>
  </section>

  <section class="card card--back" aria-label="Business card back">
    <div class="brand-back">
      <span class="brand-mark"></span>
      <p class="brand-name">MORVANE ESTATES</p>
    </div>
    <p class="website-back">www.morvaneestates.example</p>
  </section>
</main>
</body>
</html>
```